Blue Harbor Business Cards

Name Tomas Welbridge
Title Mortgage Originator
Phone (800) 614-2290 x32
Direct (571) 362-0471
Email twelbridge@blueharborhomeloans.com
NMLS #1847362
Name Lena Ortiz
Title Mortgage Originator
Location (800) 614-2290 x55
Direct (440) 276-5190
Email lortiz@blueharborhomeloans.com
NMLS #2739418
Name Desmond Holloway-Finch
Title Mortgage Originator
Location (800) 614-2290 x56
Direct (202) 634-1975
Email dhollowayfinch@blueharborhomeloans.com
NMLS #2784530
Name Rosalyn Whitaker
Title Mortgage Originator
Location (800) 614-2290 x57
Direct (240) 358-6621
Email rwhitaker@blueharborhomeloans.com
NMLS #2491086
Name Gwen Holbrook
Title Mortgage Originator
Location (800) 614-2290 x58
Direct (540) 716-2384
Email gholbrook@blueharborhomeloans.com
NMLS #2438617
Name Ravi Dunmore
Title Mortgage Originator
Location (800) 614-2290 x59
Direct (240) 563-8827
Email rdunmore@blueharborhomeloans.com
NMLS #2597142
Name Ivy Marlow
Title Mortgage Originator
Location (800) 614-2290 x60
Direct (202) 479-3306
Email ivy@ivyfindshomes.com
NMLS #2718394
Contact Information for Business Card
Name Tomas Welbridge Title Mortgage Originator Phone (800) 614-2290 x32 Direct (571) 362-0471 Email twelbridge@blueharborhomeloans.com NMLS #1847362 Name Lena Ortiz Title Mortgage Originator Location (800) 614-2290 x55 Direct (440) 276-5190 Email lortiz@blueharborhomeloans.com NMLS #2739418 Name Desmond Holloway-Finch Title Mortgage Originator Location (800) 614-2290 x56 Direct (202) 634-1975 Email dhollowayfinch@blueharborhomeloans.com NMLS #2784530 Name Rosalyn Whitaker Title Mortgage Originator Location (800) 614-2290 x57 Direct (240) 358-6621 Email rwhitaker@blueharborhomeloans.com NMLS #2491086 Name Gwen Holbrook Title Mortgage Originator Location (800) 614-2290 x58 Direct (540) 716-2384 Email gholbrook@blueharborhomeloans.com NMLS #2438617 Name Ravi Dunmore Title Mortgage Originator Location (800) 614-2290 x59 Direct (240) 563-8827 Email rdunmore@blueharborhomeloans.com NMLS #2597142 Name Ivy Marlow Title Mortgage Originator Location (800) 614-2290 x60 Direct (202) 479-3306 Email ivy@ivyfindshomes.com NMLS #2718394
Look and feel
Each slider illustrates characteristics of the customer's brand and the style your logo design should communicate.

```html
<!DOCTYPE html>
<html lang="en">
<head>
<meta charset="UTF-8">
<title>Blue Harbor Business Card – Ivy Marlow</title>
<link href="https://fonts.googleapis.com/css2?family=Great+Vibes&family=Montserrat:wght@500&family=Lato:wght@400;700&display=swap" rel="stylesheet">
<style>
  :root {
    --backdrop: #7f7f7f;
    --card: #252a3e;
    --accent: #2bbfcc;
    --text: #ffffff;
    --ring: #3b3b3d;
    --portrait-light: #f3eef0;
    --portrait-mid: #d9a9b8;
  }
  html, body {
    margin: 0;
    padding: 0;
    width: 1200px;
    height: 1000px;
    overflow: hidden;
    background: var(--backdrop);
  }
  .card {
    position: absolute;
    left: 26px;
    top: 172px;
    width: 1148px;
    height: 656px;
    border-radius: 28px;
    background: var(--card);
  }
  .portrait-frame {
    position: absolute;
    left: 116px;
    top: 160px;
    width: 366px;
    height: 366px;
    border-radius: 50%;
    background: var(--ring);
  }
  .portrait {
    position: absolute;
    left: 11px;
    top: 11px;
    width: 344px;
    height: 344px;
    border-radius: 50%;
    background: radial-gradient(circle at 50% 60%, var(--portrait-mid) 0%, var(--portrait-light) 62%);
  }
  .details {
    position: absolute;
    left: 612px;
    top: 0;
    width: 400px;
    text-align: center;
    color: var(--text);
  }
  .name {
    position: absolute;
    top: 78px;
    left: 0;
    width: 100%;
    margin: 0;
    font-family: "Great Vibes", cursive;
    font-weight: 400;
    font-size: 66px;
    line-height: 1;
    color: var(--accent);
  }
  .title {
    position: absolute;
    top: 188px;
    left: 0;
    width: 100%;
    margin: 0;
    font-family: "Montserrat", sans-serif;
    font-weight: 500;
    font-size: 25px;
    letter-spacing: 0.5px;
  }
  .icon-row {
    position: absolute;
    top: 276px;
    left: 89px;
  }
  .contact {
    position: absolute;
    left: 0;
    width: 100%;
    margin: 0;
    font-family: "Lato", sans-serif;
    font-size: 29px;
    line-height: 1;
  }
  .contact.office { top: 336px; }
  .contact.direct { top: 386px; }
  .contact.email { top: 435px; font-size: 27px; }
  .license {
    position: absolute;
    top: 507px;
    left: 83px;
    width: 235px;
    height: 49px;
    border-top: 2px solid var(--accent);
    border-bottom: 2px solid var(--accent);
    font-family: "Lato", sans-serif;
    font-weight: 700;
    font-size: 26px;
    line-height: 49px;
  }
  .license-number { color: var(--accent); }
</style>
</head>
<body>
  <main class="card">
    <div class="portrait-frame">
      <div class="portrait" role="img" aria-label="Portrait photo of Ivy Marlow in a pink blazer"></div>
    </div>

    <section class="details">
      <h1 class="name">Ivy Marlow</h1>
      <p class="title">MORTGAGE ORIGINATOR</p>

      <svg class="icon-row" width="222" height="38" viewBox="0 0 222 38" fill="none" stroke="var(--accent)" stroke-width="2">
        <line x1="0" y1="19" x2="39" y2="19" stroke-width="3"/>
        <line x1="183" y1="19" x2="222" y2="19" stroke-width="3"/>
        <rect x="48" y="2" width="35" height="34" rx="6"/>
        <rect x="93" y="2" width="35" height="34" rx="6"/>
        <rect x="138" y="2" width="35" height="34" rx="6"/>
        <rect x="59" y="8" width="13" height="22" rx="2"/>
        <line x1="63" y1="26" x2="68" y2="26"/>
        <path d="M100 17 q10.5 -8 21 0 l-2 3 h-4 v-2 h-9 v2 h-4 z" fill="var(--accent)" stroke="none"/>
        <rect x="102" y="21" width="17" height="9" rx="2" fill="var(--accent)" stroke="none"/>
        <path d="M145 19 l21 -9 -4 20 -6 -6 z M156 24 l-1 5 3 -3" fill="var(--accent)" stroke="none"/>
      </svg>

      <p class="contact office">(800) 614-2290 x60</p>
      <p class="contact direct">(202) 479-3306</p>
      <p class="contact email">ivy@ivyfindshomes.com</p>

      <div class="license">NMLS <span class="license-number">#2718394</span></div>
    </section>
  </main>
</body>
</html>
```